Velno - Website for fruit & juice

- The location of the outlet is Fort Kochi in India.
- Fort Kochi is a tourist destination. And it attracts majorly French and Portuguese tourist due to the history of the place.
- The location had plenty of food joints & mostly provide local foods only without giving much options to tourist.
- Road side fruit shops don't look hygienic
- At Velno we are going to sell fresh fruits as well as fruit juices.
- Customers can pick their fruits and Velno staffs will squeeze/blend or slice it for them.
- There will be no e-commerce on the site (no buying of products through site)

Target Market(s)

Tourist & health conscious individuals who want to have fresh fruit or juice.

Coding

Coded - Design and coding required

Number of Pages Required

4 page

Font styles to use
Script

Colors

Designer to choose colors to be used in the design.

Requirements
Must have
• Back End. Editable website.
• Since it for fruits & juices, we will be selling fruits as per season or availability.
• Editable or back end will allow us to add or delete menus as per availability.
• The project much have 4 pages. Namely:
• - Home
• - Concept
• - Menu
• - Location & Contact
Nice to have
• Fresh feel of the website
Should not have
• E-commerce

```html
<!DOCTYPE html>
<html lang="en">
<head>
<meta charset="utf-8">
<title>Velno – Fresh Fruit &amp; Juice</title>
<link href="https://fonts.googleapis.com/css2?family=Montserrat:wght@400;700&family=Raleway:wght@300;400;600&display=swap" rel="stylesheet">
<style>
:root{
  --page-bg:#ffffff;
  --ink:#2b2b2b;
  --muted:#8a8a8a;
  --green:#6cbf3c;
  --navy:#2c3e55;
  --blue:#2a9ad8;
  --red:#e0302f;
  --dark:#333333;
  --darker:#262626;
  --accent:#3aa85a;
  --light:#f1f2f1;
}
*{margin:0;padding:0;box-sizing:border-box}
html,body{width:768px;height:1200px;overflow:hidden;background:var(--page-bg)}
body{font-family:"Raleway",sans-serif;color:var(--ink);position:relative}
.site{position:absolute;left:184px;top:9px;width:400px;height:1182px;overflow:hidden;background:#fff;box-shadow:0 0 10px rgba(0,0,0,.12)}
.block{position:absolute;left:0;width:400px}
.photo{position:absolute}
.hero{top:0;height:190px;background:linear-gradient(90deg,#f4f5f5,#e9ecec)}
.hero .photo{right:0;top:0;width:154px;height:190px;background:linear-gradient(160deg,#eceeee 0%,#d98a8f 35%,#b8313f 60%,#d9583e 80%,#e7e9e9 100%)}
.hero h1{position:absolute;left:56px;top:56px;font-family:"Montserrat",sans-serif;font-weight:700;font-size:15px;line-height:16px;letter-spacing:.5px}
.hero p{position:absolute;left:56px;top:96px;width:136px;font-size:4.8px;line-height:9px;color:var(--muted)}
.hero .brand{position:absolute;left:66px;top:172px}
.slider-arrow{position:absolute;left:0;top:89px;width:13px;height:13px;background:#9a9a9a;color:#fff;font-size:8px;text-align:center;line-height:13px}
.nav{top:190px;height:14px;background:#fff;border-bottom:1px solid #eee;display:flex;align-items:center;padding:0 58px 0 61px}
.brand{font-family:"Raleway",sans-serif;font-weight:600;font-size:8px;color:var(--accent)}
.nav ul{list-style:none;display:flex;gap:9px;margin-left:auto;font-family:"Montserrat",sans-serif;font-size:3.2px;letter-spacing:.3px}
.nav li:first-child{color:var(--accent)}
.stats{top:204px;height:177px;background:linear-gradient(90deg,#a58a22,#c9b43a 30%,#6f9d2c 55%,#8fb83a 80%,#a9c24a)}
.stat{position:absolute;top:54px;width:60px;text-align:center;color:#fff}
.stat svg{display:block;margin:0 auto 6px}
.stat b{font-family:"Raleway",sans-serif;font-weight:300;font-size:13px}
.stat span{display:block;margin-top:8px;font-size:3.5px;letter-spacing:.3px;opacity:.8}
.to-top{position:absolute;right:8px;width:10px;height:10px;background:rgba(255,255,255,.3);color:#fff;font-size:6px;text-align:center;line-height:10px}
.fresh{top:381px;height:175px;background:radial-gradient(circle at 40% 50%,#d9253a,#b0162a 55%,#3a1b1f)}
.fresh h2{position:absolute;left:56px;top:74px;font-weight:300;font-size:16px;color:#fff}
.fresh p{position:absolute;left:56px;top:104px;width:160px;font-size:4.4px;line-height:9px;color:#fff}
.cards{top:556px;height:76px;display:flex}
.card{flex:none;height:76px;padding:17px 11px 0;color:#fff}
.card h3{font-family:"Montserrat",sans-serif;font-size:5px;font-weight:700;letter-spacing:.2px}
.card p{margin-top:8px;font-size:3px;line-height:5.5px;width:66px;opacity:.85}
.card a{display:inline-block;margin-top:7px;border:1px solid #fff;padding:2px 6px;font-family:"Montserrat",sans-serif;font-size:3px;font-weight:700;letter-spacing:.3px}
.quote{top:632px;height:42px;background:var(--light);display:flex;align-items:center;justify-content:center;font-family:"Montserrat",sans-serif;font-size:6.3px;letter-spacing:.3px;color:var(--ink)}
.origin{top:674px;height:176px}
.origin .photo{inset:0;background:linear-gradient(90deg,#4a4a46 0%,#7a6a3a 35%,#5a5048 60%,#8a6230 85%,#b5792a 100%)}
.origin h2{position:absolute;left:237px;top:12px;font-weight:300;font-size:16px;line-height:25px;color:#fff}
.origin p{position:absolute;left:237px;top:68px;width:110px;font-size:4.2px;line-height:9px;color:#fff}
.btn-line{position:absolute;border:1px solid #fff;color:#fff;font-family:"Montserrat",sans-serif;font-size:3.5px;font-weight:700;height:11px;line-height:9px;text-align:center;letter-spacing:.3px}
.hence{top:850px;height:170px;background:radial-gradient(ellipse at 50% 60%,#c9603a,#8a3e2e 40%,#3d4a3a 75%,#55603f)}
.hence h2{position:absolute;left:0;right:0;top:38px;text-align:center;font-weight:300;font-size:16px;color:#fff}
.hence p{position:absolute;left:56px;top:74px;width:290px;text-align:center;font-size:4.4px;line-height:9px;color:#fff}
.footer{top:1020px;height:128px;background:var(--dark);color:#cfcfcf}
.footer .col{position:absolute;top:22px;font-size:3.4px;line-height:7px}
.footer h4{font-family:"Montserrat",sans-serif;font-size:3.8px;letter-spacing:.4px;color:#fff;margin-bottom:6px}
.footer .brand{font-size:12px}
.num{font-size:7px;color:#fff}
.newsletter{display:flex;margin-top:6px}
.newsletter span{width:65px;height:9px;background:#3f3f3f;padding-left:12px;font-size:3px;line-height:9px;color:#888}
.newsletter b{width:24px;height:9px;background:var(--accent);color:#fff;font-size:3.2px;line-height:9px;text-align:center;font-weight:600}
.social{display:flex;align-items:center;gap:4px;font-size:3px;line-height:4px}
.social i{width:10px;height:10px;display:block}
.bottom{top:1148px;height:34px;background:var(--darker);font-size:3px;color:#777;line-height:5px}
</style>
</head>
<body>
<div class="site">

  <section class="block hero">
    <div class="photo" role="img" aria-label="Bowl of berries, strawberries, blood orange and rhubarb stalks"></div>
    <div class="slider-arrow">‹</div>
    <h1>HEALTHY<br>VEGETABLES</h1>
    <p>Lorem ipsum dolor sit amet, consectetur adipiscing elit, sed do eiusmod tempor incididunt ut labore et dolore magna aliqua. Ut enim ad minim veniam, quis nostrud.</p>
    <span class="brand">Velno</span>
  </section>

  <nav class="block nav">
    <span class="brand">Velno</span>
    <ul><li>HOME</li><li>ABOUT US</li><li>SERVICES</li><li>PRODUCTS</li><li>CONTACTS</li><li>⌕</li></ul>
  </nav>

  <section class="block stats">
    <div class="photo" role="img" aria-label="Close-up of yellow and green banana bunches" style="inset:0"></div>
    <div class="stat" style="left:49px"><svg width="12" height="10" viewBox="0 0 12 10"><circle cx="4" cy="3" r="2" fill="#fff"/><circle cx="8" cy="3" r="2" fill="#fff"/><path d="M0 10q4-6 8 0zM4 10q4-6 8 0z" fill="#fff"/></svg><b>1246+</b><span>HAPPY CUSTOMERS</span></div>
    <div class="stat" style="left:123px"><svg width="10" height="10" viewBox="0 0 10 10"><circle cx="5" cy="4" r="3.5" fill="#fff"/><rect x="3.5" y="7" width="3" height="3" fill="#fff"/></svg><b>2370+</b><span>DAILY DELIVERY</span></div>
    <div class="stat" style="left:197px"><svg width="12" height="11" viewBox="0 0 12 11"><rect x="0.5" y="1.5" width="11" height="9" fill="none" stroke="#fff"/><rect x="0.5" y="1.5" width="11" height="3" fill="#fff"/></svg><b>585+</b><span>SERVED EVENTS</span></div>
    <div class="stat" style="left:271px"><svg width="12" height="11" viewBox="0 0 12 11"><path d="M1 0v11M1 1h10l-2 3 2 3H1" fill="#fff" stroke="#fff"/></svg><b>39+</b><span>SOURCE LOCATIONS</span></div>
    <div class="to-top" style="top:160px">˄</div>
  </section>

  <section class="block fresh">
    <div class="photo" role="img" aria-label="Baskets of fresh raspberries" style="inset:0"></div>
    <h2>Feel Fresh</h2>
    <p>We make juice from the fresh fruits that you pick up yourself from the fruit basket.</p>
  </section>

  <section class="block cards">
    <div class="card" style="width:98px;background:var(--green)"><h3>BEST &amp; FRESH IDEAS</h3><p>Lorem ipsum dolor sit amet, consectetur adipiscing elit, sed do eiusmod.</p><a>READ MORE</a></div>
    <div class="card" style="width:102px;background:var(--navy)"><h3>POSITIVE TESTOMONIAL</h3><p>Lorem ipsum dolor sit amet, consectetur adipiscing elit, sed do eiusmod.</p><a>READ MORE</a></div>
    <div class="card" style="width:102px;background:var(--blue)"><h3>HAPPY CUSTOMERS</h3><p>Lorem ipsum dolor sit amet, consectetur adipiscing elit, sed do eiusmod.</p><a>READ MORE</a></div>
    <div class="card" style="width:98px;background:var(--red)"><h3>FRUITS FOR EVENTS</h3><p>Lorem ipsum dolor sit amet, consectetur adipiscing elit, sed do eiusmod.</p><a>READ MORE</a></div>
  </section>

  <section class="block quote">“WE AT VELNO INSIST OUR CLIENTELE TO PICK THE FRESH FRUITS THEMSELVES FROM OUR BASKETS”</section>

  <section class="block origin">
    <div class="photo" role="img" aria-label="Glass of fresh orange juice and halved oranges on a dark wooden table"></div>
    <h2>Origin of the<br>Concept</h2>
    <p>Visit any fruit vendor and ask them what they do with the left over and if you are lucky enough you may get the truth. They sell their leftovers to the juice bar. When you order a glass of juice at any place you may not have any idea about the condition of the fruit before it was squeezed and served to you. Here is where we at Velno decided to bring in transparency.</p>
    <span class="btn-line" style="left:237px;top:135px;width:42px">CONTACT US</span>
    <div class="to-top" style="top:158px">˄</div>
  </section>

  <section class="block hence">
    <div class="photo" role="img" aria-label="Bowl of sliced peaches and blueberries" style="inset:0"></div>
    <h2>And hence Velno</h2>
    <p>As a health conscious person one every right to know the fruit before she sips the last sip of juice made out of it. We at Velno insist our clientele to pick the fresh fruits themselves from our fruit baskets so they know what they are consuming. And we can blend or squeeze the fruits for them with only fruit or fruit with some add-ons. And hence we don't sell juice by bottle size; we sell it by fruits that you pick up from our fruit basket.</p>
    <span class="btn-line" style="left:166px;top:137px;width:39px">READ MORE</span>
    <span class="btn-line" style="left:210px;top:137px;width:25px;background:#fff;color:var(--ink)">BLOG</span>
  </section>

  <footer class="block footer">
    <div class="col" style="left:56px;top:24px;width:60px">
      <div class="brand" style="margin-bottom:12px">Velno</div>
      Fresh Fruit in Fort Kochi, India.<br><br>
      <b style="color:#fff">Headquarters:</b><br>22 Harbour Lane, Calvetty,<br>Fort Kochi, India<br><br>
      <b style="color:#fff">Phone:</b> (91) 0000 12345<br><b style="color:#fff">Fax:</b> (91) 0000 12346<br><b style="color:#fff">Email:</b> hello@velno.example
    </div>
    <div class="col" style="left:121px;width:50px">
      <h4>MENU</h4>
      <div style="padding-left:4px">Home<br>About us<br>Products<br>Services<br>Events<br>Contacts</div>
    </div>
    <div class="col" style="left:186px;width:62px">
      <h4>RECENT ARTICLES</h4>
      Lorem ipsum dolor sit amet, consectetur<br><span style="color:#888">12th Jun 2024</span><br><br>
      Sed accumsan vel amet dolor quis<br><span style="color:#888">10th Dec 2023</span><br><br>
      Debitis nihil placeat illum est nisi<br><span style="color:#888">02nd July 2023</span>
    </div>
    <div class="col" style="left:256px;width:100px">
      <div style="display:flex;gap:26px"><div><span class="num">1,506</span><br>CLIENTS</div><div><span class="num">184</span><br>PRODUCTS</div></div>
      <div style="margin-top:10px">Subscribe to Our Newsletter to get Important News, Amazing Offers &amp; Event Dates</div>
      <div class="newsletter"><span>Enter your Email</span><b>Subscribe</b></div>
      <div style="display:flex;gap:20px;margin-top:10px">
        <div class="social"><i style="background:#3b5a9a"></i>Like us<br>on Social</div>
        <div class="social"><i style="background:#e8772e"></i>Subscribe<br>to RSS Feeds</div>
      </div>
    </div>
  </footer>

  <div class="block bottom">
    <div style="position:absolute;left:56px;top:9px">Copyright © 2024 All Rights Reserved to Velno<br>Terms of Use / Privacy Policy</div>
    <div style="position:absolute;right:60px;top:7px;display:flex;gap:6px">
      <span style="width:3px;height:3px;border-radius:50%;background:#666"></span><span style="width:3px;height:3px;border-radius:50%;background:#666"></span><span style="width:3px;height:3px;border-radius:50%;background:#666"></span><span style="width:3px;height:3px;border-radius:50%;background:#666"></span><span style="width:3px;height:3px;border-radius:50%;background:#666"></span>
    </div>
    <div style="position:absolute;right:60px;top:14px">hello@velno.example · (91) 0000 12345 · Our Team</div>
    <div class="to-top" style="top:16px;background:#111">˄</div>
  </div>

</div>
</body>
</html>
```